"Top Hat" Ferndale Rowan Guild- Our annual benefit is an evening of fun and fundraising.

We are non-profit organization that is looking for a good theme for our fundraiser in March 11, 2023. 5:30pm- 9:30PM. We have decided It is going to be a casino night, with fun at the tables, a shopping area, 50/50 raffle and raise a paddle . Our website is https://www.ferndalerowanguild.com. We would like to see designs that have a festive theme that looks fun and not too flashy.

Target Market(s)

Ages 50+

Industry/Entity Type

Non-profit

Requirements
Nice to have
• A fun theme that is not so cheesy

```html
<!DOCTYPE html>
<html lang="en">
<head>
<meta charset="utf-8">
<title>Top Hat – Casino Night Invitation</title>
<link href="https://fonts.googleapis.com/css2?family=Cinzel:wght@700&family=Dancing+Script:wght@700&family=Josefin+Sans:wght@600&family=Playfair+Display:wght@900&family=Poppins:wght@400&display=swap" rel="stylesheet">
<style>
  :root {
    --ink: #0f0a0a;
    --ember: #4a1510;
    --gold: #ffcc00;
    --frame-gold: #c9a227;
    --white: #ffffff;
    --chip-violet: #8a4fd0;
    --chip-dark: #2a2230;
  }
  * { margin: 0; padding: 0; box-sizing: border-box; }
  html, body { width: 845px; height: 1200px; overflow: hidden; background: var(--ink); }
  .invitation {
    position: relative;
    width: 845px;
    height: 1200px;
    background: var(--ink);
    overflow: hidden;
    color: var(--white);
    text-align: center;
  }
  .fireworks-backdrop {
    position: absolute;
    inset: 0 0 auto 0;
    height: 760px;
    background:
      radial-gradient(ellipse 60% 40% at 50% 18%, #7a2418 0%, rgba(74,21,16,0.7) 45%, rgba(15,10,10,0) 100%),
      linear-gradient(180deg, #3a1410 0%, #22100d 50%, var(--ink) 100%);
  }
  .frame {
    position: absolute;
    left: 0; top: 0;
  }
  .line { position: absolute; left: 0; width: 100%; }
  .tagline {
    top: 132px;
    font-family: "Josefin Sans", sans-serif;
    font-weight: 600;
    font-size: 28px;
    letter-spacing: 1px;
    color: var(--gold);
  }
  .invite-script {
    top: 170px;
    font-family: "Dancing Script", cursive;
    font-weight: 700;
    font-size: 24px;
  }
  .host {
    top: 204px;
    font-family: "Josefin Sans", sans-serif;
    font-weight: 600;
    font-size: 24px;
    letter-spacing: 1px;
  }
  .title {
    top: 218px;
    font-family: "Playfair Display", serif;
    font-weight: 900;
    font-size: 90px;
    line-height: 1.2;
    color: var(--gold);
  }
  .chips-photo {
    position: absolute;
    left: 220px; top: 345px;
    width: 410px; height: 395px;
    border-radius: 40% 40% 30% 30%;
    background:
      radial-gradient(circle at 68% 62%, var(--chip-violet) 0%, rgba(138,79,208,0.6) 22%, rgba(0,0,0,0) 40%),
      radial-gradient(ellipse 45% 40% at 40% 40%, rgba(138,79,208,0.75) 0%, rgba(42,34,48,0.7) 60%, rgba(15,10,10,0) 100%);
  }
  .date {
    top: 620px;
    font-family: "Josefin Sans", sans-serif;
    font-weight: 600;
    font-size: 28px;
    letter-spacing: 1px;
  }
  .time { top: 656px; font-family: "Josefin Sans", sans-serif; font-weight: 600; font-size: 28px; letter-spacing: 1px; }
  .divider { position: absolute; left: 342px; width: 160px; height: 12px; }
  .feature {
    font-family: "Poppins", sans-serif;
    font-size: 19px;
  }
  .venue {
    top: 866px;
    font-family: "Cinzel", serif;
    font-weight: 700;
    font-size: 29px;
  }
  .address { top: 905px; font-family: "Poppins", sans-serif; font-size: 20px; }
  .rsvp {
    top: 978px;
    font-family: "Cinzel", serif;
    font-weight: 700;
    font-size: 36px;
  }
  .rsvp-date { top: 1026px; font-family: "Poppins", sans-serif; font-size: 20px; }
</style>
</head>
<body>
<main class="invitation">
  <div class="fireworks-backdrop" role="img" aria-label="Red and gold fireworks bursting in a night sky"></div>

  <svg class="frame" width="845" height="1200" viewBox="0 0 845 1200" aria-hidden="true">
    <rect x="38" y="34" width="769" height="1128" fill="none" stroke="var(--frame-gold)" stroke-width="2"/>
    <rect x="48" y="44" width="749" height="1108" fill="none" stroke="var(--frame-gold)" stroke-width="1.5"/>
  </svg>

  <p class="line tagline">TOP HAT</p>
  <p class="line invite-script">you are invited to attend our</p>
  <p class="line host">FERNDALE ROWAN GUILD FUNDRAISER EVENT</p>
  <h1 class="line title">Casino Night</h1>

  <div class="chips-photo" role="img" aria-label="Stacks of purple, white and black poker chips with a heart chip in front"></div>

  <p class="line date">SATURDAY, MARCH 11, 2023</p>
  <p class="line time">5:30PM- 9:30PM</p>

  <svg class="divider" style="top:700px" viewBox="0 0 160 12" aria-hidden="true">
    <line x1="0" y1="6" x2="70" y2="6" stroke="var(--gold)" stroke-width="1.5"/>
    <circle cx="80" cy="6" r="5" fill="var(--gold)"/>
    <line x1="90" y1="6" x2="160" y2="6" stroke="var(--gold)" stroke-width="1.5"/>
  </svg>

  <p class="line feature" style="top:728px">~ Fun at the table ~</p>
  <p class="line feature" style="top:762px">~ 50/50 Raffle ~</p>
  <p class="line feature" style="top:796px">~ Shopping area &amp; Raise a Paddle ~</p>

  <svg class="divider" style="top:840px" viewBox="0 0 160 12" aria-hidden="true">
    <line x1="0" y1="6" x2="70" y2="6" stroke="var(--gold)" stroke-width="1.5"/>
    <circle cx="80" cy="6" r="5" fill="var(--gold)"/>
    <line x1="90" y1="6" x2="160" y2="6" stroke="var(--gold)" stroke-width="1.5"/>
  </svg>

  <p class="line venue">Hollis Creek Country Club</p>
  <p class="line address">2450 Lantern Hill Road, Marlow Springs, CA 91400</p>

  <svg class="divider" style="top:951px" viewBox="0 0 160 12" aria-hidden="true">
    <line x1="0" y1="6" x2="70" y2="6" stroke="var(--gold)" stroke-width="1.5"/>
    <circle cx="80" cy="6" r="5" fill="var(--gold)"/>
    <line x1="90" y1="6" x2="160" y2="6" stroke="var(--gold)" stroke-width="1.5"/>
  </svg>

  <p class="line rsvp">RSVP</p>
  <p class="line rsvp-date">Before March 1, 2023</p>
</main>
</body>
</html>
```